Business Card - Business Consultancy

Newly Established Company, specializing in Business Consultancy, Human Resource Management, Talent Acquisition and Payroll Solutions.

We need a Business card design which portrays "elegance" and a very sleek yet business-like design. We would like a nice blue trimming (which goes well with the logo) to separate the content of the business card at the top. We would also like to see the design using the color silver either as a background or incorporated into it.

The final design should be a Business card which has colors matching the logo; a nice font; the above-mentioned specifics that adheres to the theme of "a stylish and professional business"

FYI: please do not have too fanciful designs.

Industry/Entity Type

Business Consultant

Contact Information for Business Card

Marcus Tellon
Business Development Director
Brightpath HR Consulting Private Limited
27 Wexford Lane, #05-03B
Harbourview Trade Tower
Singapore 061739
Mobile : (+65) 94386157
Email : mtellon@brightpathhr-advisory.com
Alternative : brightpathhradvisory@mailbox-example.com

Requirements
Must have
• Nice Blue Trimming matching Logo which separates content, see attached
• Design incorporates either a silver background or the use of the color silver
Should not have
• No Fanciful Designs
• No Childish Designs
• No Overly Complicated Designs

```html
<!DOCTYPE html>
<html lang="en">
<head>
<meta charset="utf-8">
<title>Brightpath HR Consulting – Business Card</title>
<link href="https://fonts.googleapis.com/css2?family=Source+Sans+3:wght@400;600;700&display=swap" rel="stylesheet">
<style>
  :root {
    --stage: #000000;
    --card: #ffffff;
    --brand-blue: #1b7bc0;
    --trim-blue: #3a86d6;
    --ink: #1c1c1c;
    --silver: #c9ccd1;
    --brand-grey: #4a4a4a;
  }
  * { margin: 0; padding: 0; box-sizing: border-box; }
  html, body { width: 1200px; height: 900px; overflow: hidden; }
  body {
    background: var(--stage);
    position: relative;
    font-family: "Source Sans 3", "Myriad Pro", sans-serif;
    color: var(--ink);
  }
  .card {
    position: absolute;
    top: 271px;
    width: 457px;
    height: 281px;
    background: var(--card);
    border-radius: 14px;
    overflow: hidden;
  }
  .card--front { left: 137px; }
  .card--back { left: 626px; }

  /* front */
  .brand-mark {
    position: absolute;
    left: 44px; top: 82px;
    width: 106px; height: 106px;
    border-radius: 50%;
    background: var(--brand-blue);
  }
  .brand-caption {
    position: absolute;
    left: 30px; top: 196px;
    width: 134px;
    text-align: center;
    font-size: 13px;
    font-weight: 600;
    color: var(--brand-grey);
  }
  .divider {
    position: absolute;
    left: 186px; top: 66px;
    width: 1px; height: 152px;
    background: linear-gradient(to bottom, transparent, var(--silver) 20%, var(--silver) 80%, transparent);
  }
  .details {
    position: absolute;
    left: 205px; top: 46px;
    font-size: 12.5px;
    line-height: 19px;
  }
  .details__name {
    font-size: 17px;
    font-weight: 600;
    color: var(--brand-blue);
    line-height: 22px;
  }
  .details__address { margin-top: 17px; }
  .contacts { margin-top: 13px; list-style: none; font-size: 11.5px; }
  .contacts li { display: flex; align-items: center; height: 19px; }
  .contacts svg { width: 10px; height: 10px; margin-right: 8px; fill: var(--brand-blue); flex: none; }

  /* back */
  .lockup {
    position: absolute;
    left: 100px; top: 78px;
    display: flex;
    align-items: center;
  }
  .lockup__dot {
    width: 84px; height: 84px;
    border-radius: 50%;
    background: var(--brand-blue);
    margin-right: 16px;
  }
  .lockup__name {
    font-size: 24px;
    font-weight: 700;
    line-height: 26px;
    color: var(--brand-grey);
  }
  .services {
    position: absolute;
    left: 0; right: 0; top: 215px;
    display: flex;
    align-items: center;
    font-size: 14.5px;
    font-weight: 600;
    white-space: nowrap;
  }
  .services::before, .services::after {
    content: "";
    flex: 1;
    height: 2px;
    background: var(--trim-blue);
  }
  .services span { padding: 0 6px; }
</style>
</head>
<body>

<section class="card card--front">
  <div class="brand-mark" role="img" aria-label="Brightpath HR Consulting mark"></div>
  <div class="brand-caption">Brightpath</div>
  <div class="divider"></div>
  <div class="details">
    <p class="details__name">Marcus Tellon</p>
    <p class="details__title">Business Development Director</p>
    <p class="details__address">27 Wexford Lane, #05-03B<br>Harbourview Trade Tower<br>Singapore 061739</p>
    <ul class="contacts">
      <li><svg viewBox="0 0 10 10"><path d="M2 0.5 3.6 2.6 2.7 3.6c.7 1.5 2 2.8 3.6 3.6l1-1L9.5 8 8.4 9.5C4.3 9.2.8 5.7.5 1.6Z"/></svg>(+65) 94386157</li>
      <li><svg viewBox="0 0 10 10"><path d="M0 2h10v6H0Z M0.6 2.4 5 5.6 9.4 2.4" stroke="#fff" stroke-width="0.8"/></svg>mtellon@brightpathhr-advisory.com</li>
      <li><svg viewBox="0 0 10 10"><path d="M0 2h10v6H0Z M0.6 2.4 5 5.6 9.4 2.4" stroke="#fff" stroke-width="0.8"/></svg>brightpathhradvisory@mailbox-example.com</li>
    </ul>
  </div>
</section>

<section class="card card--back">
  <div class="lockup">
    <div class="lockup__dot"></div>
    <p class="lockup__name">BRIGHTPATH<br>HR Consulting</p>
  </div>
  <p class="services"><span>Recruitment | HR Solutions | Business &nbsp;| Consultancy</span></p>
</section>

</body>
</html>
```